FernGlow Getaways Banner Advert Project

FernGlow is Australia's top weight loss retreat and we are looking for a series of banner adverts to promote our products on the websites http://www.slimharbour.example.com.au and http://www.wellnesscovesdirectory.example.com. Our customers are looking to lose weight and they want to be reassured upon seeing our advert that we can help them lose weight in a safe, secure and caring enviroment. Above all they want to be able to identify with the people attending the retreat (i.e. bigger people in images, etc). We want to convey comfort and luxury, but affordable price. We want to convey that customers will get great results and that our programs are suitable for people of all ages, shapes, sizes and fitness levels. We require the following ad size variations:

728x90
130x195
524x184

Some possible ideas/layouts are attached to brief

Target Market(s)

Predominantly women aged 30 - 50 but we do get men too and therefore the ad shouldn't be too feminine.

Industry/Entity Type

Fitness

Requirements
Must have
• Images of 'target audience' you can see some examples in photo gallery at www.fernglowgetaways.example.com.au.
• FernGlow logo needs to be in advert (maybe on a rotation - doesn't have to be there all the time. Needs to be an animated GIF (or equiv) not flash
Nice to have
• Images of facilities see at photo gallery on www.fernglowgetaways.example.com.au
Should not have
• any images of scales, tape measures, etc or thin people!

```html
<!DOCTYPE html>
<html lang="en">
<head>
<meta charset="utf-8">
<title>FernGlow Getaways – Banner Series</title>
<link rel="stylesheet" href="https://fonts.googleapis.com/css2?family=Mulish:wght@400;700;800&display=swap">
<style>
  :root {
    --page-bg: #ffffff;
    --banner-orange: #f7941d;
    --banner-orange-light: #fbb040;
    --banner-orange-deep: #e8601c;
    --headline: #ffffff;
    --pill-bg: #fde3b8;
    --pill-text: #b5121b;
    --photo-light: #f3d9c4;
    --photo-mid: #d9b89a;
    --photo-deep: #c9a27e;
  }
  html, body {
    margin: 0;
    padding: 0;
    width: 1200px;
    height: 900px;
    overflow: hidden;
    background: var(--page-bg);
  }
  .banner-series {
    position: relative;
    width: 1200px;
    height: 900px;
  }
  .banner {
    position: absolute;
    left: 52px;
    width: 1096px;
    height: 136px;
    overflow: hidden;
    background:
      radial-gradient(ellipse 420px 200px at 560px 50%, var(--banner-orange-light) 0%, rgba(251,176,64,0) 100%),
      radial-gradient(circle 150px at 40px 30%, rgba(232,96,28,0.55) 0%, rgba(232,96,28,0) 100%),
      radial-gradient(circle 170px at 960px 50%, rgba(232,96,28,0.45) 0%, rgba(232,96,28,0) 100%),
      linear-gradient(90deg, var(--banner-orange-deep) 0%, var(--banner-orange) 22%, var(--banner-orange) 78%, var(--banner-orange-deep) 100%);
    font-family: "Mulish", "Century Gothic", sans-serif;
  }
  .banner--one   { top: 138px; }
  .banner--two   { top: 298px; }
  .banner--three { top: 458px; }
  .banner--four  { top: 618px; }

  .headline {
    position: absolute;
    left: 28px;
    top: 18px;
    margin: 0;
    font-size: 29px;
    font-weight: 400;
    color: var(--headline);
    letter-spacing: -0.2px;
    white-space: nowrap;
  }
  .headline strong { font-weight: 800; }

  .benefits {
    position: absolute;
    left: 22px;
    top: 68px;
    display: flex;
    gap: 16px;
    margin: 0;
    padding: 0;
    list-style: none;
  }
  .benefit {
    height: 36px;
    width: 206px;
    box-sizing: border-box;
    border-radius: 10px;
    background: var(--pill-bg);
    color: var(--pill-text);
    font-size: 14.5px;
    font-weight: 700;
    display: flex;
    align-items: center;
    justify-content: center;
  }

  .guest-photo {
    position: absolute;
    right: 0;
    top: 0;
    width: 154px;
    height: 100%;
    background: linear-gradient(160deg, var(--photo-light) 0%, var(--photo-mid) 55%, var(--photo-deep) 100%);
  }
</style>
</head>
<body>
<main class="banner-series">

  <section class="banner banner--one">
    <h1 class="headline"><strong>Lose weight</strong> now at Australia’s Top <strong>Weight Loss Retreat</strong> &gt;&gt;</h1>
    <ul class="benefits">
      <li class="benefit">Life Changing Results</li>
    </ul>
    <div class="guest-photo" role="img" aria-label="Photo of a smiling retreat guest with a towel over her shoulders"></div>
  </section>

  <section class="banner banner--two">
    <h2 class="headline"><strong>Lose weight</strong> now at Australia’s Top <strong>Weight Loss Retreat</strong> &gt;&gt;</h2>
    <ul class="benefits">
      <li class="benefit">Life Changing Results</li>
      <li class="benefit">Suitable for everyone</li>
    </ul>
    <div class="guest-photo" role="img" aria-label="Photo of a smiling retreat guest with a towel over her shoulders"></div>
  </section>

  <section class="banner banner--three">
    <h2 class="headline"><strong>Lose weight</strong> now at Australia’s Top <strong>Weight Loss Retreat</strong> &gt;&gt;</h2>
    <ul class="benefits">
      <li class="benefit">Life Changing Results</li>
      <li class="benefit">Suitable for everyone</li>
      <li class="benefit">1st Class Facilities</li>
    </ul>
    <div class="guest-photo" role="img" aria-label="Photo of a smiling retreat guest with a towel over her shoulders"></div>
  </section>

  <section class="banner banner--four">
    <h2 class="headline"><strong>Lose weight</strong> now at Australia’s Top <strong>Weight Loss Retreat</strong> &gt;&gt;</h2>
    <ul class="benefits">
      <li class="benefit">Life Changing Results</li>
      <li class="benefit">Suitable for everyone</li>
      <li class="benefit">1st Class Facilities</li>
      <li class="benefit">Stunning Locations</li>
    </ul>
    <div class="guest-photo" role="img" aria-label="Photo of a smiling retreat guest with a towel over her shoulders"></div>
  </section>

</main>
</body>
</html>
```